Vireo M.K. - Diagnostic Ultrasound Flyer

About US
Vireo M.K. is a concierge ultrasound company that provides onsite or offsite diagnostic ultrasounds. We have over 14 years experience in sonography, business management, and customer service. We offer both the physician and patient flexibility, convenience, and access to timely services.

We provide ultrasounds for the following specialties:
Obstetrics/Gynecology
Abdominal
Small Parts
Vascular

Company Features:
1. Onsite or Offsite Scans
2. Images Available Immediately for Referring Physician and Patient
3. Flexible Options for Ultrasound Interpretation/Billing
4. Access to Interpreting Radiologist
5. Final Report Process - 1-2 Business Days/ 1 hour for STAT.
6. PACS Storage with Secure Access.

We need a place to add in our contact information (address, email, website, phone)

We already have a logo and would like to use it ( they are attached). We would the colors to match the logo colors....maybe lighter version of yellow and blue.

```html
<!DOCTYPE html>
<html lang="en">
<head>
<meta charset="utf-8">
<title>Vireo M.K. – Diagnostic Ultrasound Flyer</title>
<link href="https://fonts.googleapis.com/css2?family=Poppins:wght@400;500;600;700;800&display=swap" rel="stylesheet">
<style>
  :root {
    --page-bg: #dc8f1a;
    --blue: #3341a6;
    --blue-deep: #2a3690;
    --navy-text: #1e2766;
    --yellow: #f8bf30;
    --yellow-soft: #fbc63f;
    --orange: #f29a1c;
    --white: #ffffff;
  }
  * { margin: 0; padding: 0; box-sizing: border-box; }
  html, body { width: 1200px; height: 800px; overflow: hidden; }
  body {
    background: var(--page-bg);
    font-family: "Poppins", sans-serif;
    position: relative;
  }
  .flyer {
    position: absolute;
    left: 324px; top: 13px;
    width: 552px; height: 774px;
    background: var(--yellow-soft);
    overflow: hidden;
  }
  .top-strip { position: absolute; left: 0; top: 0; width: 100%; height: 9px; background: var(--yellow); }
  .header { position: absolute; left: 0; top: 9px; width: 100%; height: 100px; background: var(--white); }
  .brand-name {
    position: absolute; left: 32px; top: 22px;
    font-weight: 800; font-size: 44px; line-height: 1;
    color: var(--blue); letter-spacing: 1px;
  }
  .brand-tagline {
    position: absolute; left: 56px; top: 74px;
    font-size: 13px; font-weight: 500; color: #1b1b1b; letter-spacing: .2px;
  }
  .hero {
    position: absolute; left: 0; top: 109px; width: 100%; height: 329px;
    background: linear-gradient(160deg, var(--blue) 0%, var(--blue-deep) 100%);
  }
  .headline {
    position: absolute; left: 18px; top: 125px;
    color: var(--yellow); font-weight: 700; font-size: 47px; line-height: 60px;
  }
  .specialties { position: absolute; left: 18px; top: 252px; list-style: none; }
  .specialties li {
    display: flex; align-items: center; gap: 10px;
    color: var(--white); font-size: 40px; line-height: 56px; font-weight: 400;
  }
  .tick { flex: none; }
  .divider {
    position: absolute; left: 22px; top: 430px; width: 506px; height: 8px;
    border-radius: 4px; background: var(--orange);
  }
  .photo { position: absolute; }
  .photo-consult {
    left: 381px; top: 52px; width: 144px; height: 118px;
    border: 5px solid var(--yellow);
    background: linear-gradient(135deg, #e6eef5, #b9c9d8);
  }
  .photo-anatomy {
    left: 374px; top: 137px; width: 76px; height: 63px;
    border: 4px solid var(--yellow);
    background: linear-gradient(135deg, #e7b4a8, #c9706a);
  }
  .experience-badge {
    position: absolute; left: 430px; top: 150px; width: 80px; height: 80px;
    border-radius: 50%; background: var(--orange);
    display: flex; align-items: center; justify-content: center; text-align: center;
    color: var(--white); font-size: 8.5px; font-weight: 600; line-height: 11px;
  }
  .experience-badge strong { font-weight: 800; }
  .photo-machine {
    left: 365px; top: 240px; width: 168px; height: 262px;
    border-radius: 14px;
    background: linear-gradient(180deg, #c9ced8, #8c94a6);
  }
  .features {
    position: absolute; left: 17px; top: 447px; list-style: none;
    color: var(--navy-text); font-size: 15px; line-height: 24px;
  }
  .features li { display: flex; align-items: flex-start; gap: 5px; }
  .features .tick { margin-top: 7px; }
  .photo-patients {
    left: 372px; top: 588px; width: 180px; height: 186px;
    background: linear-gradient(160deg, #f3e6dc, #d8b6a4);
  }
  .contact-band {
    position: absolute; left: 0; top: 662px; width: 347px; height: 112px;
    background: var(--blue); border-top-right-radius: 22px;
  }
  .contact-band-right {
    position: absolute; left: 347px; top: 686px; width: 205px; height: 88px;
    background: var(--blue);
  }
  .contact-list {
    position: absolute; left: 26px; top: 673px; list-style: none;
    color: var(--white); font-size: 17.5px; line-height: 25px;
  }
  .contact-list li { display: flex; align-items: center; gap: 8px; }
  .call-action { position: absolute; left: 292px; top: 700px; width: 214px; height: 64px; }
  .call-label {
    position: absolute; left: 44px; top: 0; width: 160px; height: 32px;
    background: var(--white); border-radius: 16px;
    font-weight: 700; font-size: 15px; line-height: 32px; color: #1a1a1a; padding-left: 20px;
  }
  .call-number {
    position: absolute; left: 20px; top: 31px; width: 194px; height: 32px;
    background: var(--yellow); border-radius: 16px;
    font-weight: 700; font-size: 19px; line-height: 32px; color: var(--white);
    text-align: left; padding-left: 38px; white-space: nowrap;
  }
  .call-icon {
    position: absolute; left: 0; top: 6px; width: 50px; height: 50px;
    border-radius: 50%; background: var(--orange); border: 3px solid var(--white);
    display: flex; align-items: center; justify-content: center;
  }
</style>
</head>
<body>
  <main class="flyer">
    <div class="top-strip"></div>
    <header class="header">
      <div class="brand-name">VIREO M.K.</div>
      <div class="brand-tagline">CONCIERGE ULTRASOUND COMPANY</div>
    </header>

    <section class="hero"></section>
    <div class="photo photo-consult" role="img" aria-label="Doctor performing an ultrasound scan on a patient"></div>
    <div class="photo photo-anatomy" role="img" aria-label="Anatomical illustration of the abdomen"></div>
    <div class="experience-badge"><span>WE<br>HAVE OVER<br><strong>14 YEARS</strong><br>EXPERIENCE</span></div>

    <h1 class="headline">Obstetrics<br>Gynecology</h1>
    <ul class="specialties">
      <li><svg class="tick" width="22" height="22" viewBox="0 0 22 22"><circle cx="11" cy="11" r="9" fill="none" stroke="#fff" stroke-width="1.8"/><path d="M6 11l4 4 9-10" fill="none" stroke="#f8bf30" stroke-width="3" stroke-linecap="round" stroke-linejoin="round"/></svg>Abdominal</li>
      <li><svg class="tick" width="22" height="22" viewBox="0 0 22 22"><circle cx="11" cy="11" r="9" fill="none" stroke="#fff" stroke-width="1.8"/><path d="M6 11l4 4 9-10" fill="none" stroke="#f8bf30" stroke-width="3" stroke-linecap="round" stroke-linejoin="round"/></svg>Small Parts</li>
      <li><svg class="tick" width="22" height="22" viewBox="0 0 22 22"><circle cx="11" cy="11" r="9" fill="none" stroke="#fff" stroke-width="1.8"/><path d="M6 11l4 4 9-10" fill="none" stroke="#f8bf30" stroke-width="3" stroke-linecap="round" stroke-linejoin="round"/></svg>Vascular</li>
    </ul>

    <div class="divider"></div>
    <div class="photo photo-machine" role="img" aria-label="Cart-based diagnostic ultrasound machine"></div>

    <ul class="features">
      <li><svg class="tick" width="11" height="11" viewBox="0 0 22 22"><circle cx="11" cy="11" r="9" fill="none" stroke="#1e2766" stroke-width="2.5"/><path d="M6 11l4 4 9-10" fill="none" stroke="#1e2766" stroke-width="3.5" stroke-linecap="round"/></svg><span>Onsite or Offsite Scans</span></li>
      <li><svg class="tick" width="11" height="11" viewBox="0 0 22 22"><circle cx="11" cy="11" r="9" fill="none" stroke="#1e2766" stroke-width="2.5"/><path d="M6 11l4 4 9-10" fill="none" stroke="#1e2766" stroke-width="3.5" stroke-linecap="round"/></svg><span>Images Available Immediately<br>for Referring Physician and Patient</span></li>
      <li><svg class="tick" width="11" height="11" viewBox="0 0 22 22"><circle cx="11" cy="11" r="9" fill="none" stroke="#1e2766" stroke-width="2.5"/><path d="M6 11l4 4 9-10" fill="none" stroke="#1e2766" stroke-width="3.5" stroke-linecap="round"/></svg><span>Flexible Options for Ultrasound Interpretation/Billing</span></li>
      <li><svg class="tick" width="11" height="11" viewBox="0 0 22 22"><circle cx="11" cy="11" r="9" fill="none" stroke="#1e2766" stroke-width="2.5"/><path d="M6 11l4 4 9-10" fill="none" stroke="#1e2766" stroke-width="3.5" stroke-linecap="round"/></svg><span>Access to Interpreting Radiologist</span></li>
      <li><svg class="tick" width="11" height="11" viewBox="0 0 22 22"><circle cx="11" cy="11" r="9" fill="none" stroke="#1e2766" stroke-width="2.5"/><path d="M6 11l4 4 9-10" fill="none" stroke="#1e2766" stroke-width="3.5" stroke-linecap="round"/></svg><span>Final Report Process - 1-2 Business Days/ 1 hour for STAT.</span></li>
      <li><svg class="tick" width="11" height="11" viewBox="0 0 22 22"><circle cx="11" cy="11" r="9" fill="none" stroke="#1e2766" stroke-width="2.5"/><path d="M6 11l4 4 9-10" fill="none" stroke="#1e2766" stroke-width="3.5" stroke-linecap="round"/></svg><span>PACS Storage with Secure Access.</span></li>
    </ul>

    <div class="contact-band"></div>
    <div class="contact-band-right"></div>
    <div class="photo photo-patients" role="img" aria-label="Doctor with stethoscope consulting a pregnant patient"></div>

    <ul class="contact-list">
      <li><svg width="15" height="15" viewBox="0 0 16 16"><circle cx="8" cy="8" r="7" fill="none" stroke="#fff" stroke-width="1.3"/><rect x="4.3" y="5.5" width="7.4" height="5" fill="none" stroke="#fff" stroke-width="1.1"/><path d="M4.3 5.5L8 8.5l3.7-3" fill="none" stroke="#fff" stroke-width="1.1"/></svg>hello@vireomk-scans.com</li>
      <li><svg width="15" height="15" viewBox="0 0 16 16"><circle cx="8" cy="8" r="7" fill="none" stroke="#fff" stroke-width="1.3"/><ellipse cx="8" cy="8" rx="3" ry="7" fill="none" stroke="#fff" stroke-width="1.1"/><path d="M1 8h14M2.5 4.5h11M2.5 11.5h11" stroke="#fff" stroke-width="1"/></svg>www.vireomk-scans.com</li>
      <li><svg width="15" height="15" viewBox="0 0 16 16"><circle cx="8" cy="8" r="7" fill="none" stroke="#fff" stroke-width="1.3"/><path d="M8 12.5S5 9.3 5 7a3 3 0 016 0c0 2.3-3 5.5-3 5.5z" fill="none" stroke="#fff" stroke-width="1.1"/><circle cx="8" cy="7" r="1" fill="#fff"/></svg>42 Alder Row, Brookfield</li>
    </ul>

    <div class="call-action">
      <div class="call-label">CALL US NOW!</div>
      <div class="call-number">555-318-4206</div>
      <div class="call-icon">
        <svg width="24" height="24" viewBox="0 0 24 24"><path d="M6.6 2.5l3 .4 1.2 4.4-2.2 1.6c.9 2.4 2.8 4.6 5.2 5.9l1.8-2 4.2 1.5.2 3.2c-.2 1.2-1.4 2.2-2.8 2C9.5 18.7 4.6 13 4.3 5.6c0-1.6 1-2.9 2.300-3.1z" fill="#fff"/></svg>
      </div>
    </div>
  </main>
</body>
</html>
```